Transit Van Vehicle Wrap for Fenwick Meadow Gardens

We need to wrap two of our transit vans. One is a replacement. The old wrap had a back patio scene with patio furniture and lanscaping. Im not sure this is what we want moving forward. I want people to easily identify it is Fenwick Meadow Gardens when they look at the vehicle. Most recently we have wrapped our landscape trailers black, however with the base color being white and not wanting to wrap all of the vehicle, Im not sure black background is the way to go. We've also considered using 3 or 4 picture windows and a subtitle to describe what we do. We can to list words like Container Gardening, Backyard Patios, Houseplants, Plant Doctors, etc. instead of using department names to tell people what we do. We would like to use more specific words and words that formulate an image in your mind when you say it. Needs to have our logo in it. Sides and Rear doors. Rear should be logo with words or services listed. The sides could be the same or images. Ive attached two logos, one meant to be used overtop of darker background. We are a retail lifestyle garden center and landscape design build company, selling annuals, perennial, trees shrubs, lawn care items, gardening tools, house plants, pottery, patio furniture, mens and womens apparel and accessories, christmas decor and trees, lorne candles and other home fragrence, seasonal home decor and more. Visit fenwickmeadowgardens.com to see it all.

Target Market(s)

Home Owners in their 40s to 50s

Industry/Entity Type

lifestyle garden center and landscape firm

Requirements
Must have
• company logo and words describing what we do.

```html
<!DOCTYPE html>
<html lang="en">
<head>
<meta charset="utf-8">
<title>Fenwick Meadow Gardens – Van Wrap Panels</title>
<link href="https://fonts.googleapis.com/css2?family=Montserrat:wght@500;700;800&display=swap" rel="stylesheet">
<style>
  :root {
    --green: #2f8a3a;
    --green-dark: #1c5e27;
    --green-light: #6cbf45;
    --white: #ffffff;
    --ink: #2b2b2b;
    --canvas: #f4f4f4;
    --berry: #b8262c;
    --bloom: #d14f8f;
  }
  * { box-sizing: border-box; margin: 0; padding: 0; }
  html, body { width: 813px; height: 1200px; overflow: hidden; background: var(--canvas); }
  body { font-family: "Montserrat", Arial, sans-serif; position: relative; }
  .panel { position: absolute; box-shadow: 0 2px 8px rgba(0,0,0,.15); background: var(--white); }
  .panel svg { display: block; width: 100%; height: 100%; }
  .rear-doors  { left: 40px;  top: 30px;  width: 340px; height: 300px; }
  .front-hood  { left: 433px; top: 30px;  width: 340px; height: 300px; }
  .side-driver { left: 20px;  top: 370px; width: 773px; height: 300px; }
  .side-curb   { left: 20px;  top: 710px; width: 773px; height: 300px; }
  .brand { font-family: "Montserrat", Arial, sans-serif; font-weight: 800; }
  .copy  { font-family: "Montserrat", Arial, sans-serif; font-weight: 700; }
  .fine  { font-family: "Montserrat", Arial, sans-serif; font-weight: 500; }
</style>
</head>
<body>

<!-- Rear doors -->
<section class="panel rear-doors" aria-label="Rear doors wrap">
  <svg viewBox="0 0 340 300">
    <defs>
      <linearGradient id="patioTone" x1="0" y1="0" x2="0" y2="1">
        <stop offset="0" stop-color="#3d5a2c"/>
        <stop offset=".55" stop-color="#6f6a55"/>
        <stop offset="1" stop-color="#8c8372"/>
      </linearGradient>
    </defs>
    <rect width="340" height="300" fill="url(#patioTone)" role="img" aria-label="Photo of a landscaped back patio with outdoor furniture"/>
    <line x1="170" y1="0" x2="170" y2="300" stroke="rgba(0,0,0,.35)" stroke-width="2"/>
    <rect x="70" y="14" width="200" height="50" rx="4" fill="rgba(255,255,255,.92)"/>
    <circle cx="92" cy="39" r="11" fill="var(--green)"/>
    <text class="brand" x="110" y="44" font-size="12.5" fill="var(--green-dark)">Fenwick Meadow Gardens</text>
    <text class="fine" x="170" y="80" font-size="7" fill="var(--white)" text-anchor="middle">Container Gardening • Backyard Patios • Houseplants • Plant Doctors</text>
    <text class="copy" x="170" y="162" font-size="17" fill="var(--white)" text-anchor="middle">CALL: 555-014-2290</text>
    <text class="fine" x="170" y="180" font-size="9" fill="var(--white)" text-anchor="middle">fenwickmeadowgardens.com</text>
    <rect x="0" y="280" width="340" height="20" fill="var(--green-dark)"/>
  </svg>
</section>

<!-- Front hood -->
<section class="panel front-hood" aria-label="Front wrap">
  <svg viewBox="0 0 340 300">
    <rect width="340" height="300" fill="var(--white)"/>
    <rect x="0" y="0" width="340" height="22" fill="var(--green-dark)"/>
    <text class="fine" x="170" y="15" font-size="9" fill="var(--white)" text-anchor="middle">www.fenwickmeadowgardens.com</text>
    <circle cx="112" cy="92" r="8" fill="var(--green)"/>
    <text class="brand" x="125" y="96" font-size="10.5" fill="var(--green-dark)">Fenwick Meadow Gardens</text>
    <polygon points="0,190 120,215 220,215 340,190 340,300 0,300" fill="var(--green)"/>
    <polygon points="0,225 100,250 240,250 340,225 340,300 0,300" fill="var(--green-dark)"/>
    <polygon points="0,200 120,225 220,225 340,200 340,206 220,231 120,231 0,206" fill="var(--green-light)"/>
  </svg>
</section>

<!-- Driver side -->
<section class="panel side-driver" aria-label="Driver side wrap">
  <svg viewBox="0 0 773 300">
    <defs>
      <linearGradient id="hollyTone" x1="0" y1="0" x2="1" y2="1">
        <stop offset="0" stop-color="#2f6b2a"/>
        <stop offset=".5" stop-color="#4f8a33"/>
        <stop offset="1" stop-color="#7a2a24"/>
      </linearGradient>
    </defs>
    <rect width="773" height="300" fill="var(--white)"/>
    <polygon points="0,0 380,0 300,262 0,262" fill="url(#hollyTone)" role="img" aria-label="Photo of holly leaves with red berries"/>
    <polygon points="380,0 420,0 340,262 300,262" fill="var(--green)"/>
    <polygon points="420,0 440,0 360,262 340,262" fill="var(--green-light)"/>
    <circle cx="468" cy="40" r="10" fill="var(--green)"/>
    <text class="brand" x="484" y="45" font-size="14" fill="var(--green-dark)">Fenwick Meadow Gardens</text>
    <g class="contact">
      <circle cx="400" cy="112" r="9" fill="var(--green)"/>
      <path d="M396 107c1 4 3 6 7 8l2-2 2 2-2 3c-6-1-10-5-11-11l3-2 2 2z" fill="var(--white)"/>
      <text class="copy" x="416" y="119" font-size="20" fill="var(--ink)">555-014-2290</text>
      <circle cx="392" cy="143" r="7" fill="var(--green)"/>
      <text class="fine" x="405" y="147" font-size="10" fill="var(--ink)">info@fenwickmeadowgardens.com</text>
      <circle cx="386" cy="166" r="7" fill="var(--green)"/>
      <text class="fine" x="399" y="170" font-size="10" fill="var(--ink)">fenwickmeadowgardens.com</text>
      <circle cx="382" cy="196" r="8" fill="var(--green)"/>
      <circle cx="402" cy="196" r="8" fill="var(--green)"/>
      <circle cx="422" cy="196" r="8" fill="var(--green)"/>
    </g>
    <rect x="0" y="262" width="773" height="38" fill="var(--green-dark)"/>
    <text class="copy" x="386" y="286" font-size="10.5" fill="var(--white)" text-anchor="middle">RETAIL LIFESTYLE GARDEN CENTER AND LANDSCAPE DESIGN BUILD COMPANY</text>
  </svg>
</section>

<!-- Curb side -->
<section class="panel side-curb" aria-label="Curb side wrap">
  <svg viewBox="0 0 773 300">
    <defs>
      <linearGradient id="dahliaTone" x1="0" y1="0" x2="1" y2="1">
        <stop offset="0" stop-color="#7a3c6a"/>
        <stop offset=".5" stop-color="#d14f8f"/>
        <stop offset="1" stop-color="#3f6a2c"/>
      </linearGradient>
    </defs>
    <rect width="773" height="300" fill="var(--white)"/>
    <polygon points="393,0 773,0 773,262 473,262" fill="url(#dahliaTone)" role="img" aria-label="Photo of pink dahlia blooms among foliage"/>
    <polygon points="353,0 393,0 473,262 433,262" fill="var(--green)"/>
    <polygon points="333,0 353,0 433,262 413,262" fill="var(--green-light)"/>
    <circle cx="112" cy="40" r="10" fill="var(--green)"/>
    <text class="brand" x="128" y="45" font-size="14" fill="var(--green-dark)">Fenwick Meadow Gardens</text>
    <g class="contact">
      <circle cx="150" cy="112" r="9" fill="var(--green)"/>
      <path d="M146 107c1 4 3 6 7 8l2-2 2 2-2 3c-6-1-10-5-11-11l3-2 2 2z" fill="var(--white)"/>
      <text class="copy" x="166" y="119" font-size="20" fill="var(--ink)">555-014-2290</text>
      <circle cx="150" cy="143" r="7" fill="var(--green)"/>
      <text class="fine" x="163" y="147" font-size="10" fill="var(--ink)">info@fenwickmeadowgardens.com</text>
      <circle cx="150" cy="166" r="7" fill="var(--green)"/>
      <text class="fine" x="163" y="170" font-size="10" fill="var(--ink)">fenwickmeadowgardens.com</text>
      <circle cx="158" cy="196" r="8" fill="var(--green)"/>
      <circle cx="178" cy="196" r="8" fill="var(--green)"/>
      <circle cx="198" cy="196" r="8" fill="var(--green)"/>
    </g>
    <rect x="0" y="262" width="773" height="38" fill="var(--green-dark)"/>
    <text class="copy" x="386" y="286" font-size="10.5" fill="var(--white)" text-anchor="middle">RETAIL LIFESTYLE GARDEN CENTER AND LANDSCAPE DESIGN BUILD COMPANY</text>
  </svg>
</section>

</body>
</html>
```